Funky Modern Flyer A5 or Postcard size

Hi, I am looking at a one small flyer (A5 or postcard size) that I can put both on my website on the front page (ie so png) and also send out if necessary.

It has to be modern, funky and hip. My brand is professional / Corporate so it also has to fit in with that brand.

There are 6 attachments:
Example 1 - Kavorra - I like this look, clean, modern, funky and says it all.
Example 2 - Kavora - again another look I like, simple, explanatory
Example 4 - Artisan Bazaar - font is cool on this one but background not so much too much going on but I like the font
Example 5 - Example 4 - Artisan Bazaar - font is cool on this one but background not so much too much going on but I like the font
5 is my logo
Example 6 is something I found on the web this morning which is effective.

It is for a Mentoring and Training program I run called: SKYWARD

What is to be included is the following:
The name: Skyward
Somewhere: Training, Mentoring
My Logo (see attached two options) you can choose which colour suits and I have the source file should you need it
My website and email: www.deliamarsk.example / delia@deliamarsk.example

This wording: This is one of our highest in-demand programs and is based on a background and proven track record by Delia in accelerating sales organisations and their people into stand out high performers. **(NOTE this wording in this paragraph may change and I am open to you changing if you think you can make it more effective!)

Colours: white, black and gold (those are our website colours).

I'd like the Skyward to really stand out.... I have included two fonts that I really like that I got off Artisan Bazaar. However, feel free to suggest other fonts that you think cool or funky!
Updates

Hi everyone, just to add a note to the brief, I am not overly keen on pictures that are really busy. I only like a picture that is minimal and effective. The examples from Artisan Bazaar was more for the Font Style not so much the pictures in the background. The pictures can take away from a design unless done really minimally.....hope this makes sense. Delia Added Wednesday, March 15, 2017

Target Market(s)

My target Market is Corporates but I want a Funky Modern look as a lot of people in Corporates are Millennials as well which is part of my target market

Industry/Entity Type

Information Technology

Requirements
Must have
• What is to be included is the following:
• The name: Skyward
• Somewhere: Training, Mentoring
• My Logo (see attached two options) you can choose which colour suits and I have the source file should you need it
• My website and email: www.deliamarsk.example / delia@deliamarsk.example
• This wording: This is one of our highest in-demand programs and is based on a background and proven track record in high performance and accelerating sales organisations and their people into stand out high performers. (**NOTE this wording may change when final design is picked to be changed as still working in it***)
• Colours: white, black and gold (those are our website colours).
• I'd like the Skyward to really stand out.... I have included two fonts that I really like that I got off Artisan Bazaar. However, feel free to suggest other fonts that you think cool or funky! NOTE: The pictures I have attached is mainly for the FONTS not for the background pictures. I am not that keen on background pictures as it can take away from the font - unless it is minimal
Should not have
• Too many different colours, I like slick, modern, clean. White, gold and black preferred as this is our website colour.
• NOTE: The pictures from Artisan Bazaar I have attached are mainly for the FONTS not for the background pictures. I am not hugely keen on background pictures as it can take away from the font/message - unless the pictures are minimal but effective.

```html
<!DOCTYPE html>
<html lang="en">
<head>
<meta charset="utf-8">
<title>Skyward Flyer</title>
<link rel="stylesheet" href="https://fonts.googleapis.com/css2?family=Kaushan+Script&family=Questrial&display=swap">
<style>
  :root {
    --backdrop: #575757;
    --ink: #111111;
    --gold: #f2c230;
    --gold-deep: #e0a820;
    --white: #ffffff;
    --rule: #c99a1e;
  }
  html, body {
    margin: 0;
    width: 1200px;
    height: 1200px;
    overflow: hidden;
    background: var(--backdrop);
  }
  .flyer {
    position: absolute;
    left: 114px;
    top: 258px;
    width: 973px;
    height: 685px;
    overflow: hidden;
    background: var(--ink);
    font-family: "Questrial", "Century Gothic", sans-serif;
    color: var(--white);
  }
  .flyer__photo {
    position: absolute;
    inset: 0;
    background:
      radial-gradient(ellipse 190px 260px at 430px 250px, rgba(215,215,215,0.85), rgba(215,215,215,0) 100%),
      radial-gradient(ellipse 420px 260px at 160px 120px, #bdbdbd, rgba(150,150,150,0) 100%),
      linear-gradient(180deg, #8a8a8a 0%, #5c5c5c 35%, #2e2e2e 62%, #161616 100%);
  }
  .flyer__shade {
    position: absolute;
    inset: 0;
    background: linear-gradient(180deg, rgba(0,0,0,0) 55%, rgba(0,0,0,0.55) 85%, rgba(0,0,0,0.7) 100%);
  }
  .headline {
    position: absolute;
    left: 0;
    width: 973px;
    top: 208px;
    margin: 0;
    text-align: center;
    font-family: "Kaushan Script", cursive;
    font-weight: 400;
    font-size: 168px;
    line-height: 1;
    color: var(--gold);
    transform: rotate(-4deg);
    padding-left: 40px;
    box-sizing: border-box;
  }
  .headline-swash {
    position: absolute;
    left: 125px;
    top: 380px;
  }
  .services {
    position: absolute;
    left: 0;
    width: 973px;
    top: 485px;
    margin: 0;
    text-align: center;
    font-size: 27px;
    font-weight: 400;
    color: var(--gold);
    letter-spacing: 0.2px;
  }
  .services-rule {
    position: absolute;
    left: 60px;
    top: 526px;
    width: 854px;
    height: 1px;
    background: var(--rule);
  }
  .summary {
    position: absolute;
    left: 0;
    width: 973px;
    top: 542px;
    margin: 0;
    text-align: center;
    font-size: 17px;
    line-height: 22px;
  }
  .contact {
    position: absolute;
    top: 640px;
    height: 30px;
    display: flex;
    align-items: center;
    gap: 10px;
    font-size: 18px;
  }
  .contact--web { left: 208px; }
  .contact--mail { left: 510px; }
  .contact-divider {
    position: absolute;
    left: 477px;
    top: 639px;
    width: 1px;
    height: 33px;
    background: rgba(255,255,255,0.55);
  }
</style>
</head>
<body>
  <main class="flyer">
    <div class="flyer__photo" role="img" aria-label="Black and white photo of the program mentor seated on a dark sofa in a living room with framed artwork on the wall"></div>
    <div class="flyer__shade"></div>

    <h1 class="headline">Skyward</h1>
    <svg class="headline-swash" width="260" height="60" viewBox="0 0 260 60" aria-hidden="true">
      <path d="M6 44 C 70 20, 160 14, 252 12" fill="none" stroke="var(--gold)" stroke-width="4" stroke-linecap="round"/>
    </svg>

    <p class="services">Training, Mentoring</p>
    <div class="services-rule"></div>

    <p class="summary">This is one of our highest in-demand programs and is based on<br>
      a background and proven track record in high performance and accelerating sales<br>
      organisations and their people into stand out high performers.</p>

    <div class="contact contact--web">
      <svg width="26" height="26" viewBox="0 0 26 26" aria-hidden="true">
        <circle cx="13" cy="13" r="12" fill="none" stroke="var(--gold)" stroke-width="1.5"/>
        <circle cx="13" cy="13" r="7.5" fill="none" stroke="var(--gold)" stroke-width="1.4"/>
        <ellipse cx="13" cy="13" rx="3.2" ry="7.5" fill="none" stroke="var(--gold)" stroke-width="1.2"/>
        <line x1="5.5" y1="13" x2="20.5" y2="13" stroke="var(--gold)" stroke-width="1.2"/>
        <line x1="7" y1="9.5" x2="19" y2="9.5" stroke="var(--gold)" stroke-width="1"/>
        <line x1="7" y1="16.5" x2="19" y2="16.5" stroke="var(--gold)" stroke-width="1"/>
      </svg>
      <span>www.deliamarsk.example</span>
    </div>
    <div class="contact-divider"></div>
    <div class="contact contact--mail">
      <svg width="26" height="26" viewBox="0 0 26 26" aria-hidden="true">
        <circle cx="13" cy="13" r="12" fill="none" stroke="var(--gold)" stroke-width="1.5"/>
        <rect x="6.5" y="8.5" width="13" height="9" fill="var(--gold)"/>
        <path d="M6.5 8.5 L13 14 L19.5 8.5" fill="none" stroke="var(--ink)" stroke-width="1.2"/>
      </svg>
      <span>delia@deliamarsk.example</span>
    </div>
  </main>
</body>
</html>
```